Real Estate Sales Brokerage

Design a modern and fresh looking standard size business card, incorporate our logo's color scheme and modern appearance with head shot photo on front side and incorporate our log on the back side

Target Market(s)

Residential Home sales

Industry/Entity Type

Real Estate Agent

Font styles to use
Sans Serif

Colors

Designer to choose colors to be used in the design.

Requirements
Must have
• fresh, modern, not too busy, incorporate head shot in front of the card, incorporate logo in front and back of the card. Use logo design scheme as appropriate.
Nice to have
• horizontal and vertical options to compare would be nice.

```html
<!DOCTYPE html>
<html lang="en">
<head>
<meta charset="utf-8">
<title>Harborline Home Realty – Business Card</title>
<link rel="stylesheet" href="https://fonts.googleapis.com/css2?family=Cinzel:wght@500;700&family=Open+Sans:ital,wght@0,400;1,400&display=swap">
<style>
  :root {
    --backdrop: #b9b9b9;
    --olive: #434a0c;
    --olive-deep: #3a400a;
    --card-white: #f3f3f1;
    --ink: #2f2f2f;
    --cream: #f4f1e6;
    --gold: #c8b42a;
    --portrait-light: #e9e9e7;
    --portrait-mid: #c9ccd3;
    --portrait-suit: #34558f;
    --portrait-suit-deep: #243f73;
  }
  * { box-sizing: border-box; margin: 0; padding: 0; }
  html, body { width: 1200px; height: 576px; overflow: hidden; }
  body {
    background: var(--backdrop);
    position: relative;
    font-family: "Open Sans", sans-serif;
  }
  .card {
    position: absolute;
    top: 138px;
    width: 484px;
    height: 292px;
    border-radius: 14px;
    overflow: hidden;
    box-shadow: 0 3px 6px rgba(0,0,0,0.25);
  }
  .card-back { left: 82px; background: var(--olive); }
  .card-front { left: 602px; background: var(--card-white); }

  .brand {
    position: absolute;
    display: flex;
    align-items: center;
    font-family: "Cinzel", serif;
    font-weight: 500;
  }
  .brand-mark { flex: none; }
  .card-back .brand {
    left: 88px; top: 86px;
    gap: 58px;
    color: var(--cream);
    font-size: 28px;
    line-height: 27px;
  }
  .card-back .brand-mark { width: 104px; height: 104px; background: var(--gold); }
  .card-front .brand {
    left: 226px; top: 24px;
    gap: 30px;
    color: var(--olive);
    font-size: 20px;
    line-height: 19px;
  }
  .card-front .brand-mark { width: 72px; height: 72px; background: var(--olive); }

  .headshot {
    position: absolute;
    left: 0; top: 0;
    width: 222px; height: 292px;
    background:
      radial-gradient(ellipse 70% 45% at 50% 28%, var(--portrait-mid) 0%, rgba(201,204,211,0) 100%),
      linear-gradient(180deg, var(--portrait-light) 0%, var(--portrait-light) 50%, var(--portrait-suit) 68%, var(--portrait-suit-deep) 100%);
  }
  .person-name {
    position: absolute;
    left: 238px; top: 114px;
    font-family: "Cinzel", serif;
    font-weight: 700;
    font-size: 20px;
    letter-spacing: 1px;
    color: var(--olive);
  }
  .person-title {
    position: absolute;
    left: 238px; top: 144px;
    font-size: 10px;
    font-style: italic;
    color: var(--ink);
  }
  .address {
    position: absolute;
    left: 238px; top: 168px;
    font-size: 11.5px;
    line-height: 16px;
    color: var(--ink);
  }
  .contact-list {
    position: absolute;
    left: 238px; top: 208px;
    list-style: none;
    font-size: 11.5px;
    line-height: 16px;
    color: var(--ink);
  }
  .contact-list li { display: flex; align-items: center; gap: 9px; }
  .contact-list svg { width: 12px; height: 10px; fill: var(--ink); }
  .web-band {
    position: absolute;
    left: 222px; right: 0; bottom: 0;
    height: 30px;
    background: var(--olive-deep);
    color: var(--cream);
    font-size: 11.5px;
    padding-left: 16px;
    line-height: 30px;
  }
</style>
</head>
<body>
  <section class="card card-back" aria-label="Card back">
    <div class="brand">
      <span class="brand-mark"></span>
      <span class="brand-name">Harborline<br>Home<br>Realty</span>
    </div>
  </section>

  <section class="card card-front" aria-label="Card front">
    <div class="headshot" role="img" aria-label="Head shot photo of the managing director in a navy suit against a light grey backdrop"></div>
    <div class="brand">
      <span class="brand-mark"></span>
      <span class="brand-name">Harborline<br>Home<br>Realty</span>
    </div>
    <h1 class="person-name">DANIEL MORROW</h1>
    <p class="person-title">Managing Director</p>
    <p class="address">Your Long Commercial or business<br>address in 2 line with pincode</p>
    <ul class="contact-list">
      <li>
        <svg viewBox="0 0 12 10" aria-hidden="true"><path d="M0 3 Q6 -1 12 3 L10 5 L8 3.5 L4 3.5 L2 5 Z M3 5 L9 5 L11 10 L1 10 Z"/></svg>
        00-0000-000-000
      </li>
      <li>
        <svg viewBox="0 0 12 10" aria-hidden="true"><path d="M0 0 H12 V10 H0 Z M1 1.5 V9 H11 V1.5 L6 5.5 Z" fill-rule="evenodd"/></svg>
        daniel@harborlinehomerealty.com
      </li>
    </ul>
    <div class="web-band">www.harborlinehomerealty.com</div>
  </section>
</body>
</html>
```